Movie \ Film Poster for "The Sparrow Remembers Winter"

Movie / film poster, Promotional Poster. A short film about a Goldfish living in a gilded cage longing for a better life. He befriends a common House Fly and the two discuss their respective life situations. The Fly leaves and Goldfish is ultimately unfulfilled in his dreams of a better life. Script attached below. The final design should communicate with a handwritten slow calligraphy, flowing, warmth welcoming, safety comfort. Images / drawings should communicate an ennui, daily monotony, Loneliness, Envy, confinement, isolation, boredom within an otherwise fish's paradise.

Target Market(s)

USA and English Family film goers and Film Festivals Age range 12+

Industry/Entity Type

Movie Theater

Font styles to use
Script

Requirements
Must have
• Suitable for direct printing to a wall poster / theater promotional material.

```html
<!DOCTYPE html>
<html lang="en">
<head>
<meta charset="utf-8">
<title>The Sparrow Remembers Winter</title>
<link rel="stylesheet" href="https://fonts.googleapis.com/css2?family=Montserrat:wght@700&family=Allura&display=swap">
<style>
  :root {
    --deep-top: #0a4190;
    --deep-mid: #021226;
    --abyss: #020407;
    --abyss-low: #06142a;
    --title-cyan: #00f6ff;
    --title-blue: #0aa0ff;
    --script-pale: #fff8b0;
    --script-gold: #ffe500;
    --subject-gold: #f3c21e;
    --subject-amber: #b9780a;
  }
  * { margin: 0; padding: 0; box-sizing: border-box; }
  html, body { width: 813px; height: 1200px; overflow: hidden; background: var(--abyss); }
  .poster {
    position: relative;
    width: 813px;
    height: 1200px;
    overflow: hidden;
    background: linear-gradient(180deg, var(--deep-top) 0%, var(--deep-mid) 28%, var(--abyss) 52%, var(--abyss) 82%, var(--abyss-low) 100%);
  }
  .title-block {
    position: absolute;
    top: 72px;
    left: 0;
    width: 100%;
    text-align: center;
    font-family: "Montserrat", sans-serif;
    font-weight: 700;
    font-size: 100px;
    line-height: 100px;
    letter-spacing: -1px;
  }
  .title-line {
    display: block;
    background: linear-gradient(90deg, var(--title-cyan) 0%, var(--title-blue) 100%);
    -webkit-background-clip: text;
    background-clip: text;
    color: transparent;
  }
  .title-script {
    position: absolute;
    top: 290px;
    left: 0;
    width: 100%;
    text-align: center;
    font-family: "Allura", cursive;
    font-size: 250px;
    line-height: 300px;
    background: linear-gradient(180deg, var(--script-pale) 10%, var(--script-gold) 90%);
    -webkit-background-clip: text;
    background-clip: text;
    color: transparent;
  }
  .thought-bubbles {
    position: absolute;
    left: 0;
    top: 0;
    width: 813px;
    height: 1200px;
    pointer-events: none;
  }
  .subject-art {
    position: absolute;
    left: 90px;
    top: 660px;
    width: 610px;
    height: 460px;
    border-radius: 50%;
    background: radial-gradient(ellipse at 62% 48%, var(--subject-gold) 0%, var(--subject-amber) 45%, rgba(60, 40, 4, 0.35) 68%, rgba(0, 0, 0, 0) 75%);
    filter: blur(6px);
  }
</style>
</head>
<body>
  <main class="poster">
    <h1 class="title-block">
      <span class="title-line">The Sparrow</span>
      <span class="title-line">Remembers</span>
    </h1>
    <div class="title-script">Winter</div>
    <svg class="thought-bubbles" viewBox="0 0 813 1200" aria-hidden="true">
      <g fill="none" stroke="#ffe93a" stroke-width="3.5">
        <circle cx="648" cy="550" r="31"/>
        <circle cx="675" cy="663" r="17"/>
        <circle cx="640" cy="756" r="10.5"/>
      </g>
    </svg>
    <div class="subject-art" role="img" aria-label="Soft-focus photograph of a golden fish swimming toward the viewer in dark water"></div>
  </main>
</body>
</html>
```